Data Compass Plan- Brennal Insurance providing specialist Cyber and Liability Insurance

for Managed Technology Service Providers and their customer, we will use a letterhead that white labels insurer documents, which can be used in our physical letters as well as to be used within Email signatures.

Target Market(s)

Managed Technology Services Providers

Industry/Entity Type

Cyber Insurance

Requirements
Must have
• website, email address, contact phone numbers

```html
<!DOCTYPE html>
<html lang="en">
<head>
<meta charset="utf-8">
<title>Data Compass Plan – Stationery</title>
<link rel="stylesheet" href="https://fonts.googleapis.com/css2?family=Open+Sans:wght@400;600;700&display=swap">
<style>
  :root {
    --green: #3bb54a;
    --ink: #4a4a4a;
    --text: #333333;
    --paper: #ffffff;
    --backdrop: #c6c6c6;
    --sign-tone: #e4e4e4;
  }
  * { box-sizing: border-box; margin: 0; padding: 0; }
  html, body { width: 1126px; height: 1200px; overflow: hidden; }
  body {
    position: relative;
    background: var(--backdrop);
    font-family: "Open Sans", Arial, sans-serif;
    color: var(--text);
  }
  .icon-defs { position: absolute; width: 0; height: 0; }

  /* Letterhead */
  .letterhead {
    position: absolute;
    top: 28px;
    width: 470px;
    height: 665px;
    background: var(--paper);
    box-shadow: 0 4px 14px rgba(0,0,0,.18);
  }
  .letterhead--filled { left: 70px; }
  .letterhead--blank { left: 586px; }
  .wordmark {
    display: flex;
    align-items: center;
    gap: 8px;
    font-weight: 600;
    color: var(--ink);
    white-space: nowrap;
  }
  .wordmark__square { background: var(--green); flex: none; }
  .letterhead .wordmark {
    position: absolute;
    top: 46px;
    right: 40px;
    font-size: 25px;
    letter-spacing: .5px;
  }
  .letterhead .wordmark__square { width: 12px; height: 12px; }
  .letterhead__insurer {
    position: absolute;
    top: 100px;
    left: 56px;
    font-size: 10.5px;
    color: var(--green);
  }
  .letter-body {
    position: absolute;
    top: 132px;
    left: 56px;
    width: 360px;
    font-size: 7.4px;
    line-height: 1.5;
  }
  .letter-body p { margin-bottom: 9px; }
  .letter-body .sign-off { margin-top: 14px; margin-bottom: 4px; }
  .signature-mark {
    width: 60px;
    height: 14px;
    background: var(--sign-tone);
    margin-bottom: 5px;
  }
  .letter-body .signer { font-size: 6.8px; text-transform: uppercase; }

  .letter-footer {
    position: absolute;
    left: 40px;
    right: 34px;
    bottom: 30px;
    display: flex;
    align-items: flex-end;
    justify-content: space-between;
    font-size: 9px;
    line-height: 1.35;
  }
  .letter-footer__divider {
    width: 10px;
    height: 34px;
    align-self: center;
  }
  .contact-list { list-style: none; text-align: right; }
  .contact-list li { display: flex; align-items: center; justify-content: flex-end; gap: 4px; }
  .contact-list svg { width: 8px; height: 8px; fill: var(--green); }
  .letterhead__band {
    position: absolute;
    left: 0; right: 0; bottom: 0;
    height: 12px;
    background: var(--green);
  }

  /* Email signature */
  .email-signature {
    position: absolute;
    left: 43px;
    top: 740px;
    width: 1040px;
    height: 348px;
    background: var(--paper);
    box-shadow: 0 4px 14px rgba(0,0,0,.18);
  }
  .email-signature .wordmark {
    position: absolute;
    left: 140px;
    top: 150px;
    font-size: 38px;
    letter-spacing: 1px;
  }
  .email-signature .wordmark__square { width: 18px; height: 18px; }
  .email-signature__divider {
    position: absolute;
    left: 627px;
    top: 56px;
    width: 2px;
    height: 238px;
    background: var(--green);
  }
  .contact-card {
    position: absolute;
    left: 662px;
    top: 50px;
    font-size: 19px;
    line-height: 1.3;
  }
  .contact-card__name {
    font-size: 26px;
    font-weight: 700;
    color: var(--green);
    line-height: 1.1;
  }
  .contact-card__role { margin-top: 2px; }
  .contact-card__address { margin-top: 16px; }
  .contact-card__links { list-style: none; margin-top: 14px; }
  .contact-card__links li { display: flex; align-items: center; gap: 10px; height: 25px; }
  .contact-card__links svg { width: 16px; height: 16px; fill: var(--green); }
  .social-row { display: flex; gap: 6px; margin-top: 16px; }
  .social-row span {
    width: 17px; height: 17px;
    border-radius: 50%;
    background: var(--green);
  }
  .email-signature__band {
    position: absolute;
    left: 0; right: 0; bottom: 0;
    height: 23px;
    background: var(--green);
  }
</style>
</head>
<body>

<svg class="icon-defs" aria-hidden="true">
  <symbol id="icon-phone" viewBox="0 0 24 24"><path d="M6.6 10.8a15 15 0 0 0 6.6 6.6l2.2-2.2a1 1 0 0 1 1-.25 11.4 11.4 0 0 0 3.6.57 1 1 0 0 1 1 1V20a1 1 0 0 1-1 1A17 17 0 0 1 3 4a1 1 0 0 1 1-1h3.5a1 1 0 0 1 1 1c0 1.25.2 2.45.57 3.57a1 1 0 0 1-.25 1z"/></symbol>
  <symbol id="icon-mail" viewBox="0 0 24 24"><path d="M2 5h20v14H2z M2 5l10 7 10-7" /><path d="M2 6.5l10 7 10-7V5H2z" fill="#fff"/></symbol>
  <symbol id="icon-globe" viewBox="0 0 24 24"><path d="M12 2a10 10 0 1 0 0 20 10 10 0 0 0 0-20zm0 2c1.2 1.4 2 3.6 2.2 7H9.8C10 7.6 10.8 5.4 12 4zm-2.2 9h4.4c-.2 3.4-1 5.6-2.2 7-1.2-1.4-2-3.6-2.2-7zM4.1 11A8 8 0 0 1 8.6 4.7 13 13 0 0 0 7.8 11zm0 2h3.7c.1 2.4.4 4.5.8 6.3A8 8 0 0 1 4.1 13zm12.1 0h3.7a8 8 0 0 1-4.5 6.3c.4-1.8.7-3.9.8-6.3zm0-2a13 13 0 0 0-.8-6.3A8 8 0 0 1 19.9 11z"/></symbol>
</svg>

<!-- Letterhead with letter -->
<article class="letterhead letterhead--filled">
  <div class="wordmark"><span class="wordmark__square"></span>Data Compass Plan</div>
  <div class="letterhead__insurer">Brennal Insurance</div>
  <div class="letter-body">
    <p>Thank you for choosing us to protect your managed services business. This letter confirms that your cyber and liability cover is now active, and that our team has reviewed the details you provided during your application with care.</p>
    <p>Your policy schedule sets out the limits, excess and territories that apply to each section. Please read it closely and keep it with your records, as it forms part of the contract between you and the insurer named within.</p>
    <p>If a client system is breached or data is lost, call our claims line at once. Early notice lets us bring in response experts quickly and limits the harm to you, your staff and the customers who rely on you.</p>
    <p>We will contact you before renewal to review your services, contracts and security controls. Any change in the work you do, or the size of your client base, may affect your cover and should be shared with us early.</p>
    <p>Should you have any questions about this letter or your policy, please reach out by phone or email. We value your trust and look forward to supporting your business for many years to come.</p>
    <p class="sign-off">Sincerely</p>
    <div class="signature-mark" role="img" aria-label="Handwritten signature"></div>
    <p class="signer">Nadia Corlett</p>
  </div>
  <footer class="letter-footer">
    <address style="font-style:normal">4180 Linden Quay<br>Harbor Westmere<br>CA 92000</address>
    <svg class="letter-footer__divider" viewBox="0 0 10 34"><line x1="9" y1="1" x2="1" y2="33" stroke="#3bb54a" stroke-width="1.6"/></svg>
    <div>ABN no. 41 203 586 110<br>Corporate Authorised<br>Representative no. 3305174</div>
    <svg class="letter-footer__divider" viewBox="0 0 10 34"><line x1="9" y1="1" x2="1" y2="33" stroke="#3bb54a" stroke-width="1.6"/></svg>
    <ul class="contact-list">
      <li>555 210 487 <svg><use href="#icon-phone"/></svg></li>
      <li>info@dcplan.example <svg><use href="#icon-mail"/></svg></li>
      <li>www.dcplan.example <svg><use href="#icon-globe"/></svg></li>
    </ul>
  </footer>
  <div class="letterhead__band"></div>
</article>

<!-- Blank letterhead -->
<article class="letterhead letterhead--blank">
  <div class="wordmark"><span class="wordmark__square"></span>Data Compass Plan</div>
  <div class="letterhead__insurer">Brennal Insurance</div>
  <footer class="letter-footer">
    <address style="font-style:normal">4180 Linden Quay<br>Harbor Westmere<br>CA 92000</address>
    <svg class="letter-footer__divider" viewBox="0 0 10 34"><line x1="9" y1="1" x2="1" y2="33" stroke="#3bb54a" stroke-width="1.6"/></svg>
    <div>ABN no. 41 203 586 110<br>Corporate Authorised<br>Representative no. 3305174</div>
    <svg class="letter-footer__divider" viewBox="0 0 10 34"><line x1="9" y1="1" x2="1" y2="33" stroke="#3bb54a" stroke-width="1.6"/></svg>
    <ul class="contact-list">
      <li>555 210 487 <svg><use href="#icon-phone"/></svg></li>
      <li>info@dcplan.example <svg><use href="#icon-mail"/></svg></li>
      <li>www.dcplan.example <svg><use href="#icon-globe"/></svg></li>
    </ul>
  </footer>
  <div class="letterhead__band"></div>
</article>

<!-- Email signature -->
<section class="email-signature">
  <div class="wordmark"><span class="wordmark__square"></span>Data Compass Plan</div>
  <div class="email-signature__divider"></div>
  <div class="contact-card">
    <div class="contact-card__name">NADIA CORLETT</div>
    <div class="contact-card__role">Co-Founder</div>
    <div class="contact-card__address">4180 Linden Quay Harbor<br>Westmere CA 92000</div>
    <ul class="contact-card__links">
      <li><svg><use href="#icon-phone"/></svg>555-010-487-210</li>
      <li><svg><use href="#icon-mail"/></svg>team@dcplan.example</li>
      <li><svg><use href="#icon-globe"/></svg>www.dcplan.example</li>
    </ul>
    <div class="social-row" aria-label="Social links">
      <span></span><span></span><span></span><span></span>
    </div>
  </div>
  <div class="email-signature__band"></div>
</section>

</body>
</html>
```